Building Company Business Card Design

Need a design for a business card:
It needs to have: Name, Phone, Facebook link, Website, email
i would also like a list of works we undertake:
-New Homes
-Extensions, Renovations & Bathrooms
-Decking, Carports, Sheds (Residential and Industrial)
-Carpentry
-Fences, Patios & Pergolas

Name, Phone, Facebook link, Website, email + details of services provided listed in description

```html
<!DOCTYPE html>
<html lang="en">
<head>
<meta charset="utf-8">
<title>Ridgeline Homes – Business Card</title>
<link href="https://fonts.googleapis.com/css2?family=Arimo:wght@400;700&display=swap" rel="stylesheet">
<style>
  :root {
    --page: #e6e6e6;
    --card-white: #f4f4f4;
    --green: #1fa04a;
    --green-name: #3fae6a;
    --green-deep: #137a35;
    --grey-band: #7d7d7d;
    --ink: #1c1c1c;
    --text-grey: #555555;
    --rule: #6a6a6a;
    --white: #ffffff;
  }
  * { margin: 0; padding: 0; box-sizing: border-box; }
  html, body {
    width: 1200px; height: 1040px; overflow: hidden;
    background: var(--page);
    font-family: "Arimo", Arial, sans-serif;
  }
  .canvas { position: relative; width: 1200px; height: 1040px; }

  .card {
    position: absolute; left: 280px; width: 640px; height: 366px;
    border-radius: 18px; overflow: hidden;
    box-shadow: 0 2px 4px rgba(0,0,0,0.25);
  }
  .card--front { top: 130px; background: var(--card-white); }
  .card--back { top: 567px; height: 370px; background: var(--green); }

  /* front */
  .brand {
    position: absolute; right: 42px; top: 98px;
    display: flex; align-items: center; gap: 10px;
  }
  .brand__mark { width: 18px; height: 18px; background: var(--green); }
  .brand__name {
    font-weight: 700; font-size: 28px; letter-spacing: 0.5px;
    color: var(--ink); text-transform: uppercase;
  }
  .person { position: absolute; left: 45px; top: 196px; }
  .person__name { font-weight: 700; font-size: 24px; color: var(--green-name); }
  .person__role { font-size: 16px; color: var(--text-grey); margin-top: 2px; }
  .divider {
    position: absolute; left: 45px; top: 250px; width: 553px;
    height: 1px; background: var(--rule);
  }
  .contacts { position: absolute; left: 45px; top: 260px; list-style: none; }
  .contacts li {
    display: flex; align-items: center; gap: 7px;
    font-size: 16px; color: var(--text-grey); height: 19.5px;
  }
  .contacts svg { width: 13px; height: 13px; flex: none; }
  .band { position: absolute; left: 0; bottom: 0; width: 640px; height: 42px; }
  .website {
    position: absolute; right: 40px; bottom: 16px;
    font-size: 15.5px; color: var(--white);
  }

  /* back */
  .back-brand {
    position: absolute; left: 0; right: 0; top: 145px;
    display: flex; justify-content: center; align-items: center; gap: 14px;
  }
  .back-brand__mark { width: 30px; height: 30px; background: var(--green-deep); }
  .back-brand__name {
    font-weight: 700; font-size: 46px; letter-spacing: 1px;
    color: var(--green-deep); text-transform: uppercase;
  }
  .services {
    position: absolute; left: 0; right: 0; top: 270px;
    text-align: center; color: var(--white); font-size: 16px; line-height: 19px;
  }
  .services .dot {
    display: inline-block; width: 5px; height: 5px; background: var(--white);
    margin: 0 10px 2px; vertical-align: middle;
  }
</style>
</head>
<body>
<main class="canvas">

  <section class="card card--front" aria-label="Business card front">
    <div class="brand">
      <span class="brand__mark"></span>
      <span class="brand__name">Ridgeline Homes</span>
    </div>

    <div class="person">
      <p class="person__name">Marcus Hale</p>
      <p class="person__role">President</p>
    </div>
    <div class="divider"></div>

    <ul class="contacts">
      <li>
        <svg viewBox="0 0 24 24" aria-hidden="true"><path fill="#3fae6a" d="M6.6 10.8a15.1 15.1 0 0 0 6.6 6.6l2.2-2.2c.3-.3.7-.4 1-.2 1.1.4 2.3.6 3.6.6.6 0 1 .4 1 1V20c0 .6-.4 1-1 1A17 17 0 0 1 3 4c0-.6.4-1 1-1h3.5c.6 0 1 .4 1 1 0 1.3.2 2.5.6 3.6.1.3 0 .7-.2 1z"/></svg>
        (555) 0142-7781
      </li>
      <li>
        <svg viewBox="0 0 24 24" aria-hidden="true"><rect x="2" y="5" width="20" height="14" fill="none" stroke="#3fae6a" stroke-width="2"/><path d="M2 5l10 8 10-8" fill="none" stroke="#3fae6a" stroke-width="2"/></svg>
        info@ridgelinehomes.com
      </li>
      <li>
        <svg viewBox="0 0 24 24" aria-hidden="true"><circle cx="12" cy="12" r="11" fill="#3fae6a"/></svg>
        @ridgelinehomes.com
      </li>
    </ul>

    <svg class="band" viewBox="0 0 640 42" preserveAspectRatio="none" aria-hidden="true">
      <polygon points="371,0 640,0 640,42 0,42 0,28 347,28" fill="#1fa04a"/>
      <polygon points="0,10 358,10 341,28 0,28" fill="#7d7d7d"/>
    </svg>
    <p class="website">www.ridgelinehomes.com</p>
  </section>

  <section class="card card--back" aria-label="Business card back">
    <div class="back-brand">
      <span class="back-brand__mark"></span>
      <span class="back-brand__name">Ridgeline Homes</span>
    </div>
    <div class="services">
      <p>New Homes<span class="dot"></span>Extensions, Renovations &amp; Bathrooms</p>
      <p>Decking, Carports, Sheds (Residential and Industrial)</p>
      <p>Carpentry<span class="dot"></span>Fences, Patios &amp; Pergolas</p>
    </div>
  </section>

</main>
</body>
</html>
```